New Vidloom Channel Banner Graphic/Logo for "Quiet Loft Home Studio"

Create a banner for my new Vidloom channel for Quiet Loft Home Studio. This is partially a logo project, but the logo will not be used elsewhere. Check out Vidloom channels to see the banners others have created. This channel is about my home studio, the gear, microphones, musical instruments, wiring, software etc. that goes into a home studio. It's a free channel, made for sharing information. This is a graphic design that will be posted on vidloom using built-in vidloom tools.
Updates

More information about this project! I'm staring a channel called "Quiet Loft Home Studio" on vidloom.example. I need a deign for this banner and a logo for Quiet Loft Home Studio. I called the channel by that name because my music studio is my happy place. It's about music and instruments (gutars, piano, drums, percussion) singing (microhpones), creativity, and what you'd expect form musicians. It's also about technology, recording, live-streaming, music videos, etc. It is my hobby, not my profession. I will be creating content for other amateur home studio aficionados and hobbyists. There are a lot of home studio channels and videos you can look at on vidloom to get a flavor for musicians and studios. Usually fairly tech-heavy. An appeal of my channel will be a very approachable, "i'm the same as you" welcome for people that are doing it to enjoy it.

I put this project in the wrong category to start. This has been fixed, but I think benefits I would have received (such as invited designers) and announcement of project in the correct category mean I'm not getting designers. Your initial menu should be improved. I'm having a banner created for a web page in Vidloom. I think it is easy to mistake that for a web design when it is really a graphic design for the web.

Target Market(s)

Similar to myself, people as interested in studio/production tech as they are in making music, perhaps trending a bit older and successful enough to afford some gear!

Number of Pages Required

1 page

Font styles to use
Sans Serif

Requirements
Must have
• This is not really a web design, i may have miscategorized. Please see uploaded docs for pics of similar banner on a Vidloom page. ADDED 1/5: As this is a vidloom channel that could be viewed on any device, the banner should be friendly in this way and design or design variations needed for PC, Tabro, phone vie3wing.

Here are the Vidloom size specs:
Banner image guidelines
Your banner image must meet the following criteria:

Minimum dimension for upload: 2048 x 1152 px with an aspect ratio of 16:9.
At the Minimum dimension, the safe area for text and logos: 1235 x 338 px. Larger images may get cropped on certain views or devices.
File size: 6 MB or smaller.
How to resize images

You can use your computer's image editor or an online image resizer to resize the images. For example, you can use Glimpser on an Pearcore computer or Brightsoft Snaps on Panes.

```html
<!DOCTYPE html>
<html lang="en">
<head>
<meta charset="utf-8">
<title>Quiet Loft Home Studio – Channel Banner</title>
<link rel="stylesheet" href="https://fonts.googleapis.com/css2?family=Josefin+Sans:wght@400&family=Open+Sans:ital,wght@0,400;1,400&display=swap">
<style>
  :root {
    --bg-deep: #1a120c;
    --bg-mid: #3b2a1e;
    --bg-warm: #6b5443;
    --bg-light: #b7a797;
    --text-main: #ffffff;
    --text-soft: #e9e2da;
    --tag-fill: #9a4d17;
    --tag-edge: #b8611f;
  }
  html, body {
    margin: 0;
    padding: 0;
    width: 1200px;
    height: 198px;
    overflow: hidden;
    background: var(--bg-deep);
  }
  .banner {
    position: relative;
    width: 1200px;
    height: 198px;
    overflow: hidden;
    font-family: "Open Sans", Arial, sans-serif;
    color: var(--text-main);
  }
  .studio-photo {
    position: absolute;
    inset: 0;
    background:
      radial-gradient(ellipse 180px 140px at 470px 60px, rgba(183,167,151,0.75), rgba(183,167,151,0) 100%),
      radial-gradient(ellipse 160px 110px at 640px 80px, rgba(150,130,112,0.55), rgba(150,130,112,0) 100%),
      linear-gradient(90deg, var(--bg-deep) 0%, var(--bg-mid) 22%, var(--bg-warm) 40%, var(--bg-warm) 58%, var(--bg-mid) 75%, var(--bg-deep) 100%);
  }
  .studio-photo::after {
    content: "";
    position: absolute;
    inset: 0;
    background: linear-gradient(180deg, rgba(20,14,10,0.15) 0%, rgba(20,14,10,0.45) 100%);
  }
  .brand {
    position: absolute;
    left: 0;
    top: 0;
    width: 100%;
    height: 130px;
  }
  .brand-name {
    position: absolute;
    left: 380px;
    top: 20px;
    width: 420px;
    margin: 0;
    font-family: "Josefin Sans", Arial, sans-serif;
    font-weight: 400;
    color: var(--text-main);
    text-align: center;
    line-height: 1;
  }
  .brand-name .name-main {
    display: block;
    font-size: 62px;
    letter-spacing: 1px;
  }
  .brand-name .name-sub {
    display: block;
    margin-top: 8px;
    padding-left: 150px;
    font-size: 22px;
    letter-spacing: 2.5px;
    text-transform: uppercase;
    text-align: left;
  }
  .byline {
    position: absolute;
    left: 735px;
    top: 97px;
    font-family: "Josefin Sans", Arial, sans-serif;
    font-size: 11px;
    color: var(--text-main);
  }
  .tagline {
    position: absolute;
    left: 0;
    top: 133px;
    width: 1200px;
    margin: 0;
    text-align: center;
    font-style: italic;
    font-size: 12px;
    color: var(--text-soft);
  }
  .tag-list {
    position: absolute;
    top: 165px;
    left: 265px;
    display: flex;
    gap: 9px;
    margin: 0;
    padding: 0;
    list-style: none;
  }
  .tag {
    height: 18px;
    line-height: 18px;
    padding: 0 6px;
    background: var(--tag-fill);
    border: 1px solid var(--tag-edge);
    font-size: 9.5px;
    color: var(--text-main);
    white-space: nowrap;
  }
</style>
</head>
<body>
  <main class="banner">
    <div class="studio-photo" role="img" aria-label="Photo of a warm, dim home studio with acoustic guitars, a wooden desk, headphones, a keyboard and a condenser microphone"></div>

    <header class="brand">
      <h1 class="brand-name">
        <span class="name-main">Quiet Loft</span>
        <span class="name-sub">Home Studio</span>
      </h1>
      <span class="byline">by Dale Brenner</span>
    </header>

    <p class="tagline">A Regular Joe Blowin’ his Dough on Gear and Guitars</p>

    <ul class="tag-list">
      <li class="tag">Music + Gear + Livestreaming + Recording + DAW + Instruments + Vidloom</li>
      <li class="tag">Follow my Studio Renovation | Free How-To’s</li>
      <li class="tag">QuietLoftHomeStudio@postlane.example</li>
    </ul>
  </main>
</body>
</html>
```